Redesign of the UI of a customer service platform

To improve the user experience of our customers, we need a new design for our agent interface of our customer service platform (quillvane.com).
The focus will be on the dashboard and the inbox screens (see attached) along with the common UI elements (Buttons, menu, fonts, forms...)
We want a simple and distinctive design

Target Market(s)

Worldwide

Industry/Entity Type

It Service

Number of Pages Required

3 page

Font styles to use
Sans Serif

Requirements
Must have
• New Onboarding page: this is a new page that is shown to user the first time they login to the platform. This will replace the current onboarding screen (setup SMS, Setup widget...etc)
• Dashboard page: to access important information and activate services (see screenshot from current site)
• Inbox page: to manage all the interactions with customers. (see screenshot from current site)
• UI elements (buttons, menus, forms, tables, fonts, color palette)

```html
<!DOCTYPE html>
<html lang="en">
<head>
<meta charset="utf-8">
<title>quillvane — Dashboard</title>
<link href="https://fonts.googleapis.com/css2?family=Roboto:wght@300;400;500&display=swap" rel="stylesheet">
<style>
:root{
  --bg:#e6e7e5;
  --panel:#ffffff;
  --panel-soft:#f5f5f5;
  --panel-grey:#d4d4d4;
  --sidebar:#3a3a3a;
  --sidebar-line:#4a4a4a;
  --blue:#5aabef;
  --ink:#444444;
  --ink-soft:#666666;
  --ink-faint:#9a9a9a;
  --line:#e2e2e2;
  --alert:#f04e23;
  --white:#ffffff;
}
*{box-sizing:border-box;margin:0;padding:0}
html,body{width:1200px;height:712px;overflow:hidden}
body{font-family:'Roboto',sans-serif;background:var(--bg);color:var(--ink);position:relative}
svg{display:block}

.topbar{position:absolute;left:0;top:0;width:1200px;height:56px;background:var(--white);box-shadow:0 2px 4px rgba(0,0,0,.15);z-index:2;display:flex;align-items:center}
.brand{width:136px;padding-left:11px;display:flex;align-items:center;gap:5px;font-weight:500;font-size:19px;color:#333;letter-spacing:-.2px}
.brand-dot{width:18px;height:18px;border-radius:50%;background:#333}
.menu-toggle{margin-left:21px;width:21px}
.page-title{margin-left:22px;font-size:17px;color:#333}
.top-actions{margin-left:auto;display:flex;gap:34px;align-items:center;padding-right:30px}
.top-action{position:relative}
.count{position:absolute;top:-8px;right:-8px;width:15px;height:15px;border-radius:50%;background:var(--alert);color:#fff;font-size:10px;line-height:15px;text-align:center}

.sidebar{position:absolute;left:0;top:56px;width:136px;height:656px;background:var(--sidebar)}
.nav-item{height:90px;border-bottom:1px solid var(--sidebar-line);display:flex;flex-direction:column;align-items:center;justify-content:center;gap:8px;color:var(--white);font-size:14px;position:relative}
.nav-item.active{background:var(--blue);border-bottom:none}
.nav-item.active::after{content:"";position:absolute;right:-9px;top:36px;border-left:9px solid var(--blue);border-top:9px solid transparent;border-bottom:9px solid transparent}

.stat{position:absolute;top:70px;width:247px;height:169px;background:var(--panel);border:1px solid var(--line);text-align:center}
.stat-icon{width:52px;height:52px;border:1px solid var(--blue);border-radius:50%;margin:13px auto 0;display:flex;align-items:center;justify-content:center}
.stat-value{font-size:26px;font-weight:300;color:#333;margin-top:9px}
.stat-label{font-size:13.5px;font-weight:300;color:var(--ink-soft);line-height:19px;margin-top:6px}

.reports{position:absolute;left:153px;top:253px;width:445px;height:424px;background:var(--panel)}
.panel-head{height:47px;background:var(--panel-soft);border-bottom:1px solid var(--line);display:flex;align-items:center;padding-left:16px;font-size:17px;color:#333}
.tabs{margin-left:auto;display:flex;height:100%}
.tab{width:44px;display:flex;align-items:center;justify-content:center}
.tab.active{background:var(--white);border-top:3px solid var(--blue)}
.report-summary{height:90px;padding:20px 16px;position:relative}
.report-title{font-size:13.5px;color:var(--ink-soft)}
.report-sub{font-size:11px;color:var(--ink-faint);margin-top:8px}
.chart-switch{position:absolute;right:16px;top:27px;display:flex;border:1px solid #ccc}
.chart-switch span{width:39px;height:26px;display:flex;align-items:center;justify-content:center}
.chart-switch span:first-child{background:#e6e6e6;border-right:1px solid #ccc}
.video{height:240px;position:relative;background:linear-gradient(135deg,#d9dde4 0%,#b7bfcc 45%,#8e97a6 75%,#c9ccd1 100%)}
.play{position:absolute;left:190px;top:88px;width:66px;height:66px;border-radius:50%;background:rgba(50,50,50,.85);border:2px solid #eee;display:flex;align-items:center;justify-content:center}
.controls{position:absolute;left:21px;right:20px;bottom:16px;display:flex;align-items:center;gap:12px;color:#fff;font-size:11px}
.track{flex:1;height:2px;background:#fff;position:relative}
.track i{position:absolute;left:0;top:0;height:2px;width:63%;background:#333}
.track b{position:absolute;left:63%;top:-4px;width:9px;height:9px;border-radius:50%;background:#fff}
.caption{padding:18px 11px;font-size:12px;color:var(--ink)}

.plan{position:absolute;left:612px;top:253px;width:570px;height:443px;background:var(--panel-grey)}
.plan .panel-head{padding-right:14px}
.btn-primary{margin-left:auto;background:var(--blue);color:#fff;font-size:12px;font-weight:500;padding:7px 15px;border:none}
.addons{position:absolute;top:61px;left:14px;display:flex;gap:12px}
.addon{width:173px;height:120px;background:var(--panel);text-align:center;position:relative;padding-top:22px}
.addon .count{top:10px;right:11px;width:19px;height:19px;line-height:19px;font-size:11px}
.addon-name{font-size:13.5px;color:var(--ink-soft);margin-top:12px}
.addon-limit{font-size:12px;color:var(--ink-faint);margin-top:6px}
.services{position:absolute;left:14px;top:193px;width:542px;height:235px;background:#f7f7f7;padding-top:4px}
.service{height:75px;position:relative;padding:11px 18px;border-left:3px solid var(--panel-grey);margin-bottom:0}
.service-name{font-size:13px;color:var(--ink)}
.service-desc{font-size:11.5px;color:var(--ink-faint);line-height:17px;margin-top:6px;width:330px}
.status{position:absolute;right:22px;top:26px;background:var(--blue);color:#fff;font-size:9px;padding:3px 8px;display:flex;align-items:center;gap:4px}
</style>
</head>
<body>

<header class="topbar">
  <div class="brand"><span class="brand-dot"></span>quillvane</div>
  <svg class="menu-toggle" width="21" height="15" viewBox="0 0 21 15"><rect width="21" height="2" fill="#444"/><rect y="6.5" width="21" height="2" fill="#444"/><rect y="13" width="21" height="2" fill="#444"/></svg>
  <h1 class="page-title" style="font-weight:400">Dashboard</h1>
  <div class="top-actions">
    <div class="top-action">
      <svg width="20" height="16" viewBox="0 0 20 16"><path d="M1 8h5l1.5 3h5L14 8h5v8H1z" fill="#333"/><path d="M10 0v7M7 4l3 3 3-3" stroke="#333" stroke-width="2" fill="none"/></svg>
      <span class="count">1</span>
    </div>
    <svg width="22" height="22" viewBox="0 0 22 22"><path d="M13 1l8 8-12 12-8-8z" fill="none" stroke="#333" stroke-width="2.5"/><path d="M9 9l4 4" stroke="#333" stroke-width="2"/></svg>
  </div>
</header>

<nav class="sidebar">
  <div class="nav-item active">
    <svg width="28" height="18" viewBox="0 0 28 18"><path d="M3 17a11 11 0 1 1 22 0" fill="none" stroke="#fff" stroke-width="2.5"/><path d="M14 15l5-7" stroke="#fff" stroke-width="2.5"/><circle cx="14" cy="15" r="2" fill="#fff"/></svg>
    Dashboard
  </div>
  <div class="nav-item">
    <svg width="26" height="22" viewBox="0 0 26 22"><path d="M1 11h7l2 3h6l2-3h7v11H1z" fill="#fff"/><path d="M13 0v9M9 5l4 4 4-4" stroke="#fff" stroke-width="2.5" fill="none"/></svg>
    Inbox
  </div>
  <div class="nav-item">
    <svg width="28" height="28" viewBox="0 0 28 28"><path d="M17 2l9 9-15 15-9-9z" fill="none" stroke="#fff" stroke-width="3"/><path d="M12 12l4 4" stroke="#fff" stroke-width="2.5"/></svg>
    Tickets
  </div>
  <div class="nav-item">
    <svg width="30" height="22" viewBox="0 0 30 22"><circle cx="15" cy="6" r="5" fill="#fff"/><path d="M6 22c0-7 4-9 9-9s9 2 9 9z" fill="#fff"/><circle cx="6" cy="8" r="3.5" fill="#fff"/><circle cx="24" cy="8" r="3.5" fill="#fff"/><path d="M0 19c0-5 2-7 5-7h2c-1 2-2 4-2 7zM30 19c0-5-2-7-5-7h-2c1 2 2 4 2 7z" fill="#fff"/></svg>
    Clients
  </div>
  <div class="nav-item">
    <svg width="26" height="24" viewBox="0 0 26 24"><rect x="2" y="16" width="3" height="7" fill="#fff"/><rect x="7" y="12" width="3" height="11" fill="#fff"/><rect x="12" y="14" width="3" height="9" fill="#fff"/><rect x="17" y="9" width="3" height="14" fill="#fff"/><path d="M1 13l7-7 5 4 10-9M17 1h6v6" stroke="#fff" stroke-width="2.5" fill="none"/></svg>
    Reports
  </div>
  <div class="nav-item">
    <svg width="26" height="26" viewBox="0 0 26 26"><circle cx="13" cy="13" r="8" fill="none" stroke="#fff" stroke-width="5" stroke-dasharray="4.2 2.1"/><circle cx="13" cy="13" r="7" fill="none" stroke="#fff" stroke-width="3"/></svg>
    Settings
  </div>
</nav>

<section class="stat" style="left:154px">
  <div class="stat-icon"><svg width="20" height="28" viewBox="0 0 20 28"><circle cx="10" cy="7" r="6" fill="var(--blue)"/><path d="M1 28v-8q0-6 9-6t9 6v8z" fill="var(--blue)"/></svg></div>
  <div class="stat-value">0/0</div>
  <p class="stat-label">Lorem Ipsum is<br>simply dummy text</p>
</section>
<section class="stat" style="left:413px">
  <div class="stat-icon"><svg width="26" height="26" viewBox="0 0 28 28"><path d="M17 2l9 9-15 15-9-9z" fill="none" stroke="var(--blue)" stroke-width="3"/><path d="M12 12l4 4" stroke="var(--blue)" stroke-width="2.5"/></svg></div>
  <div class="stat-value">0/0</div>
  <p class="stat-label">Lorem Ipsum is<br>simply dummy text</p>
</section>
<section class="stat" style="left:674px">
  <div class="stat-icon"><svg width="28" height="22" viewBox="0 0 28 22"><ellipse cx="11" cy="9" rx="11" ry="8" fill="var(--blue)"/><path d="M3 14l-2 6 7-4z" fill="var(--blue)"/><ellipse cx="19" cy="12" rx="9" ry="7" fill="var(--blue)" stroke="#fff" stroke-width="1.5"/></svg></div>
  <div class="stat-value">0/0</div>
  <p class="stat-label">Lorem Ipsum is<br>simply dummy text</p>
</section>
<section class="stat" style="left:934px">
  <div class="stat-icon"><svg width="22" height="28" viewBox="0 0 22 28"><rect x="1" y="1" width="14" height="26" rx="2" fill="none" stroke="var(--blue)" stroke-width="2"/><rect x="9" y="8" width="12" height="9" rx="1" fill="var(--blue)"/><circle cx="8" cy="23" r="1.3" fill="var(--blue)"/></svg></div>
  <div class="stat-value">0/0</div>
  <p class="stat-label">Lorem Ipsum is<br>simply dummy text</p>
</section>

<section class="reports">
  <div class="panel-head">Reports
    <div class="tabs">
      <div class="tab"><svg width="16" height="20" viewBox="0 0 16 20"><rect x="1" y="1" width="10" height="18" rx="1.5" fill="none" stroke="#999" stroke-width="2"/><rect x="7" y="6" width="9" height="7" fill="#999"/></svg></div>
      <div class="tab"><svg width="22" height="18" viewBox="0 0 28 22"><ellipse cx="11" cy="9" rx="11" ry="8" fill="#999"/><ellipse cx="19" cy="12" rx="9" ry="7" fill="#999" stroke="#f5f5f5" stroke-width="1.5"/></svg></div>
      <div class="tab"><svg width="20" height="20" viewBox="0 0 28 28"><path d="M17 2l9 9-15 15-9-9z" fill="#999"/><path d="M12 12l4 4" stroke="#f5f5f5" stroke-width="2.5"/></svg></div>
      <div class="tab active"><svg width="14" height="19" viewBox="0 0 20 28"><circle cx="10" cy="7" r="6" fill="var(--blue)"/><path d="M1 28v-8q0-6 9-6t9 6v8z" fill="var(--blue)"/></svg></div>
    </div>
  </div>
  <div class="report-summary">
    <p class="report-title">Lorem Ipsum is simply dummy text</p>
    <p class="report-sub">Lorem Ipsum is simply dummy text</p>
    <div class="chart-switch">
      <span><svg width="20" height="14" viewBox="0 0 20 14"><path d="M1 0v13h19" stroke="#666" fill="none"/><path d="M5 12V5M8 12V3M11 12V6M14 12V4" stroke="#666" stroke-width="1.5"/></svg></span>
      <span><svg width="20" height="14" viewBox="0 0 20 14"><path d="M1 0v13h19" stroke="#aaa" fill="none"/><path d="M3 11l5-5 3 3 7-7" stroke="#aaa" fill="none"/></svg></span>
    </div>
  </div>
  <div class="video" role="img" aria-label="Video still: hand with a pencil reviewing printed bar and pie charts">
    <div class="play"><svg width="22" height="26" viewBox="0 0 22 26"><path d="M2 1l19 12L2 25z" fill="#fff"/></svg></div>
    <div class="controls"><span>2:31</span><div class="track"><i></i><b></b></div><span>-1:56</span></div>
  </div>
  <p class="caption">Lorem Ipsum is simply dummy</p>
</section>

<section class="plan">
  <div class="panel-head">Plan &amp; Add-ons <button class="btn-primary">Upgrade</button></div>
  <div class="addons">
    <div class="addon"><span class="count">1</span>
      <svg style="margin:0 auto" width="30" height="22" viewBox="0 0 30 22"><circle cx="15" cy="6" r="5" fill="#333"/><path d="M6 22c0-7 4-9 9-9s9 2 9 9z" fill="#333"/><circle cx="6" cy="8" r="3.5" fill="#333"/><circle cx="24" cy="8" r="3.5" fill="#333"/><path d="M0 19c0-5 2-7 5-7h2c-1 2-2 4-2 7zM30 19c0-5-2-7-5-7h-2c1 2 2 4 2 7z" fill="#333"/></svg>
      <p class="addon-name">Lorem Ipsum</p><p class="addon-limit">Unlimited</p></div>
    <div class="addon"><span class="count">1</span>
      <svg style="margin:0 auto" width="26" height="22" viewBox="0 0 26 24"><rect x="2" y="16" width="3" height="7" fill="#333"/><rect x="7" y="12" width="3" height="11" fill="#333"/><rect x="12" y="14" width="3" height="9" fill="#333"/><rect x="17" y="9" width="3" height="14" fill="#333"/><path d="M1 13l7-7 5 4 10-9M17 1h6v6" stroke="#333" stroke-width="2.5" fill="none"/></svg>
      <p class="addon-name">Lorem Ipsum</p><p class="addon-limit">Unlimited</p></div>
    <div class="addon"><span class="count">1</span>
      <svg style="margin:0 auto" width="26" height="22" viewBox="0 0 26 22"><path d="M1 11h7l2 3h6l2-3h7v11H1z" fill="#333"/><path d="M13 0v9M9 5l4 4 4-4" stroke="#333" stroke-width="2.5" fill="none"/></svg>
      <p class="addon-name">Lorem Ipsum</p><p class="addon-limit">Unlimited</p></div>
  </div>
  <div class="services">
    <div class="service"><p class="service-name">Lorum Ipsum</p><p class="service-desc">Pellentesque habitant morbi tristique senectus et netus et malesuada fames ac turpis egestas. morbi...</p>
      <span class="status"><svg width="8" height="7" viewBox="0 0 8 7"><path d="M1 3.5l2 2 4-4.5" stroke="#fff" stroke-width="1.4" fill="none"/></svg>Activted</span></div>
    <div class="service"><p class="service-name">Lorum Ipsum</p><p class="service-desc">Pellentesque habitant morbi tristique senectus et netus et malesuada fames ac turpis egestas. morbi...</p>
      <span class="status"><svg width="8" height="7" viewBox="0 0 8 7"><path d="M1 3.5l2 2 4-4.5" stroke="#fff" stroke-width="1.4" fill="none"/></svg>Activted</span></div>
    <div class="service"><p class="service-name">Lorum Ipsum</p><p class="service-desc">Pellentesque habitant morbi tristique senectus et netus et malesuada fames ac turpis egestas. morbi...</p>
      <span class="status"><svg width="8" height="7" viewBox="0 0 8 7"><path d="M1 3.5l2 2 4-4.5" stroke="#fff" stroke-width="1.4" fill="none"/></svg>Activted</span></div>
  </div>
</section>

</body>
</html>
```